Allergy Social Media Advertising Graphics Needed

We already have the copy written for ZV and Velmorix ads and need a designer to ad a graphic element to the campaign.

Target Market(s)

Mostly soccer moms, suburban Washington, DC, highly educated, smart and research oriented.

Font styles to use
Sans Serif

Requirements
Must have
• An eye-catching concept that makes people stop scrolling and pay attention to the advertisement.
Nice to have
• Clean and simple design. Bold approach with an elegant feel.
Should not have
• Too busy or cartoon-like designs.

```html
<!DOCTYPE html>
<html lang="en">
<head>
<meta charset="utf-8">
<title>ZV and Velmorix Ads – Hollis Allergy</title>
<link rel="stylesheet" href="https://fonts.googleapis.com/css2?family=Archivo:wght@500;700;800&family=Source+Sans+3:wght@400;500&display=swap">
<style>
  :root{
    --brand-blue:#0860a3;
    --brand-purple:#352c7a;
    --paper:#ffffff;
    --nut-light:#eee6da;
    --nut-mid:#d9cbb8;
    --nut-dark:#c7b59e;
    --shadow:rgba(0,0,0,.35);
    --display:"Archivo", Arial, sans-serif;
    --wordmark:"Source Sans 3", Arial, sans-serif;
  }
  *{box-sizing:border-box;margin:0;padding:0}
  html,body{width:1200px;height:593px;overflow:hidden;background:var(--paper)}
  .board{position:relative;width:1200px;height:593px;background:var(--paper);font-family:var(--display)}
  .board__panel{position:absolute;left:0;top:0;width:570px;height:593px;background:var(--brand-blue);border-radius:0 6px 6px 0}
  .board__title{position:absolute;top:70px;font-size:38px;font-weight:800;letter-spacing:.3px;line-height:1}
  .board__title--on-blue{right:calc(1200px - 565px);color:var(--paper)}
  .board__title--on-white{left:574px;color:var(--brand-blue)}

  .ad{position:absolute;top:139px;height:314px;overflow:hidden;box-shadow:0 6px 14px var(--shadow)}
  .ad--wide{left:120px;width:600px}
  .ad--square{left:757px;width:321px}
  .ad__texture{position:absolute;inset:0;background:
    radial-gradient(circle at 20% 30%,var(--nut-light) 0 18%,transparent 40%),
    radial-gradient(circle at 85% 80%,var(--nut-dark) 0 10%,transparent 35%),
    linear-gradient(135deg,var(--nut-light),var(--nut-mid) 55%,var(--nut-light))}
  .ad__shape{position:absolute;inset:0}

  .ad__logo{position:absolute;left:0;background:var(--paper);color:var(--brand-purple);font-family:var(--wordmark);font-weight:500;line-height:.95;display:flex;align-items:center}
  .ad__logo-square{background:var(--brand-purple);flex:none}
  .ad--wide .ad__logo{top:13px;width:175px;height:45px;padding-left:10px;gap:12px;font-size:17px}
  .ad--wide .ad__logo-square{width:32px;height:32px}
  .ad--square .ad__logo{top:12px;width:137px;height:29px;padding-left:21px;gap:6px;font-size:10.5px}
  .ad--square .ad__logo-square{width:19px;height:19px}

  .ad__question-band{position:absolute;left:0;top:125px;width:290px;height:65px;background:var(--brand-blue)}
  .ad__question{font-weight:700;text-transform:uppercase}
  .ad--wide .ad__question{position:absolute;left:10px;top:134px;color:var(--paper);font-size:11.5px;line-height:14px}
  .ad--square .ad__question{position:absolute;left:118px;top:53px;color:var(--brand-purple);font-size:8.6px;line-height:10px}
  .ad--square .ad__question b{color:var(--brand-blue)}

  .ad__answer-band{position:absolute;left:0;background:var(--paper)}
  .ad--wide .ad__answer-band{top:218px;width:460px;height:66px}
  .ad--square .ad__answer-band{top:253px;width:215px;height:47px}
  .ad__answer{position:absolute;font-weight:500;color:var(--brand-purple);text-transform:uppercase}
  .ad__answer b{font-weight:800;color:var(--brand-blue)}
  .ad--wide .ad__answer{left:10px;top:237px;font-size:15px;line-height:18px}
  .ad--square .ad__answer{left:4px;top:267px;font-size:11px;line-height:12.5px}

  .ad__cta{position:absolute;background:var(--brand-purple);color:var(--paper);font-weight:500;border-radius:0 999px 999px 0;display:flex;align-items:center;justify-content:center;text-transform:uppercase}
  .ad--wide .ad__cta{left:470px;top:226px;width:90px;height:24px;font-size:9px}
  .ad--square .ad__cta{left:250px;top:280px;width:57px;height:17px;font-size:6px;border-radius:999px}
</style>
</head>
<body>
<main class="board">
  <div class="board__panel"></div>
  <h1 class="board__title board__title--on-blue">ZV</h1>
  <h1 class="board__title board__title--on-white">AND VELMORIX ADS</h1>

  <article class="ad ad--wide">
    <div class="ad__texture" role="img" aria-label="Soft background of pale mixed nuts"></div>
    <div class="ad__question-band"></div>
    <div class="ad__answer-band"></div>
    <svg class="ad__shape" viewBox="0 0 600 314">
      <defs>
        <linearGradient id="wide-photo" x1="0" y1="0" x2="1" y2="0.6">
          <stop offset="0" stop-color="#4a2c22"/>
          <stop offset=".18" stop-color="#c98f72"/>
          <stop offset=".4" stop-color="#eef0ec"/>
          <stop offset=".62" stop-color="#b9d3dc"/>
          <stop offset=".8" stop-color="#d9a688"/>
          <stop offset="1" stop-color="#3b2520"/>
        </linearGradient>
        <linearGradient id="wide-photo-floor" x1="0" y1="0" x2="0" y2="1">
          <stop offset=".55" stop-color="#e6c9a4" stop-opacity="0"/>
          <stop offset="1" stop-color="#d8b48a" stop-opacity=".9"/>
        </linearGradient>
      </defs>
      <g role="img" aria-label="Photo of a mother and daughter feeding each other yogurt at a table">
        <path d="M172 0 L600 0 L600 82 L470 252 Q405 325 340 262 L185 100 Q158 62 172 0 Z" fill="url(#wide-photo)"/>
        <path d="M172 0 L600 0 L600 82 L470 252 Q405 325 340 262 L185 100 Q158 62 172 0 Z" fill="url(#wide-photo-floor)"/>
      </g>
      <path d="M185 100 L340 262 Q405 325 470 252 L600 82" fill="none" stroke="var(--brand-purple)" stroke-width="4"/>
      <path d="M180 96 L337 266 Q405 332 473 256 L600 90" fill="none" stroke="var(--brand-blue)" stroke-width="2"/>
    </svg>
    <div class="ad__logo"><span class="ad__logo-square"></span><span>hollis<br>allergy</span></div>
    <p class="ad__question">Is worrying about your<br>child’s peanut allergy<br>driving you nuts?</p>
    <p class="ad__answer">Oral <b>Immunotherapy</b><br>could <b>help</b>.</p>
    <a class="ad__cta">Learn more.</a>
  </article>

  <article class="ad ad--square">
    <div class="ad__texture" role="img" aria-label="Soft background of pale mixed nuts"></div>
    <div class="ad__answer-band"></div>
    <svg class="ad__shape" viewBox="0 0 321 314">
      <defs>
        <linearGradient id="square-photo" x1="0" y1="0" x2="1" y2="0.8">
          <stop offset="0" stop-color="#f3f4f2"/>
          <stop offset=".35" stop-color="#e9ece9"/>
          <stop offset=".55" stop-color="#b8d2dc"/>
          <stop offset=".72" stop-color="#d7a283"/>
          <stop offset="1" stop-color="#3b2520"/>
        </linearGradient>
        <linearGradient id="square-photo-floor" x1="0" y1="0" x2="0" y2="1">
          <stop offset=".6" stop-color="#e6c9a4" stop-opacity="0"/>
          <stop offset="1" stop-color="#d8b48a" stop-opacity=".9"/>
        </linearGradient>
      </defs>
      <g role="img" aria-label="Photo of a girl eating yogurt from her mother's hand">
        <path d="M150 0 L321 0 L321 205 L245 292 Q213 324 180 292 L58 175 Q35 150 55 120 Z" fill="url(#square-photo)"/>
        <path d="M150 0 L321 0 L321 205 L245 292 Q213 324 180 292 L58 175 Q35 150 55 120 Z" fill="url(#square-photo-floor)"/>
      </g>
      <path d="M150 0 L55 120 Q35 150 58 175 L180 292 Q213 324 245 292 L321 205" fill="none" stroke="var(--brand-purple)" stroke-width="2.5"/>
      <path d="M321 213 L248 297" fill="none" stroke="var(--brand-blue)" stroke-width="2"/>
    </svg>
    <div class="ad__logo"><span class="ad__logo-square"></span><span>hollis<br>allergy</span></div>
    <p class="ad__question">Is <b>worrying</b><br>about your<br>child’s <b>peanut</b><br><b>allergy</b><br>driving you <b>nuts?</b></p>
    <p class="ad__answer">Oral <b>Immunotherapy</b><br>could <b>help</b>.</p>
    <a class="ad__cta">Learn more.</a>
  </article>
</main>
</body>
</html>
```